Design our branded business card!

We'd love for you to design our business card and come up with a fitting design that reflects the Pivex brand. We're a growing tech startup with big ambitions. We've included our brand guidelines (contain colour palette), logo (EPS vector in CMYK) and old designs to help you on your way.

We'd like to keep the design fairly simple:

* Name
* Phone number
* Email address
* Website (www.pivex.life)
* Twitter (@pivex)
* Address (18 Wexham Row, Leeds, UK, LS9 4ZQ).

This would need to include print and cutting marks.

If you have any questions just let us know!

Target Market(s)

Businesses, Press and our customers!

Industry/Entity Type

Business

Contact Information for Business Card

* Name
* Phone number
* Email address
* Twitter (@pivex)

Font styles to use
Sans Serif

Requirements
Must have
• 1. Must have the Pivex logo included.
• 2. Must use the font 'Brandon Text' in either 'light' or 'thin' (https://www.typevault-demo.com/fonts/qrsfonts/halden-sans/)
• 3. Must use exact colours references from the brand guidelines. Colours outside of the brand guidelines will be discounted. White (transparent) backgrounds are fine.
• 4. Must contain the following information:
• * Name
• * Phone number
• * Email address
• * Website (www.pivex.life)
• * Twitter (@pivex)
• * Address (18 Wexham Row, Leeds, UK, LS9 4ZQ).
Nice to have
• Must use the font 'Brandon Text' in either 'light' or 'thin' (https://www.typevault-demo.com/fonts/qrsfonts/halden-sans/)
Should not have
• Colours outside of the brand guidelines will be discounted. White (transparent) backgrounds are fine.
• Avoid creating icons or including photography.

```html
<!DOCTYPE html>
<html lang="en">
<head>
<meta charset="utf-8">
<title>Pivex business card</title>
<link rel="stylesheet" href="https://fonts.googleapis.com/css2?family=Jost:wght@300;400;500;600&display=swap">
<style>
  :root {
    --brand-green: #80c477;
    --paper: #ffffff;
    --ink: #3b3e3d;
    --backdrop: #3c3c3c;
  }
  * { margin: 0; padding: 0; box-sizing: border-box; }
  html, body {
    width: 1105px;
    height: 1200px;
    overflow: hidden;
    background: var(--backdrop);
    font-family: "Jost", sans-serif;
  }
  .sheet { position: relative; width: 1105px; height: 1200px; }

  .card {
    position: absolute;
    left: 196px;
    width: 720px;
    height: 413px;
    overflow: hidden;
  }
  .card--front { top: 145px; background: var(--brand-green); color: var(--paper); }
  .card--back  { top: 602px; background: var(--paper); }

  .front-curve {
    position: absolute;
    left: 0; top: 0;
    width: 720px; height: 413px;
  }

  .wordmark {
    position: absolute;
    font-weight: 400;
    letter-spacing: 1px;
    line-height: 1;
  }
  .card--front .wordmark {
    right: 38px;
    top: 30px;
    font-size: 82px;
    color: var(--paper);
  }

  .details {
    position: absolute;
    right: 39px;
    top: 152px;
    text-align: right;
  }
  .details__name {
    font-size: 27px;
    font-weight: 600;
    line-height: 36px;
  }
  .details__address {
    margin-top: 12px;
    font-size: 18px;
    font-weight: 400;
    line-height: 27px;
  }
  .contact-list {
    list-style: none;
    margin-top: 18px;
    margin-right: -30px;
  }
  .contact-list__item {
    display: flex;
    justify-content: flex-end;
    align-items: center;
    gap: 12px;
    font-size: 18.5px;
    font-weight: 400;
    line-height: 27.5px;
  }
  .contact-list__icon { width: 18px; height: 18px; flex: none; }

  .brand-lockup {
    position: absolute;
    left: 156px;
    top: 168px;
    display: flex;
    align-items: center;
    gap: 20px;
  }
  .brand-lockup__dot {
    width: 104px;
    height: 104px;
    border-radius: 50%;
    background: var(--brand-green);
  }
  .card--back .wordmark {
    position: static;
    font-size: 80px;
    color: var(--ink);
    margin-top: -10px;
  }
</style>
</head>
<body>
<main class="sheet">

  <section class="card card--front" aria-label="Business card front">
    <svg class="front-curve" viewBox="0 0 720 413" aria-hidden="true">
      <circle cx="62" cy="297" r="325" fill="var(--paper)"/>
    </svg>

    <div class="wordmark">pivex</div>

    <div class="details">
      <p class="details__name">Alex Marlow</p>
      <p class="details__address">18 Wexham Row<br>Leeds, UK, LS9 4ZQ</p>
      <ul class="contact-list">
        <li class="contact-list__item">614 208 3759
          <svg class="contact-list__icon" viewBox="0 0 18 18" aria-hidden="true">
            <path d="M4 1.5l3 3.2-1.6 2.1c.9 2 2.4 3.5 4.3 4.4l2.1-1.6 3.2 3-1.6 2.7C7.8 15 3 10.2 1.2 3.1z" fill="var(--paper)"/>
          </svg>
        </li>
        <li class="contact-list__item">name@pivex.life
          <svg class="contact-list__icon" viewBox="0 0 18 18" aria-hidden="true">
            <rect x="1" y="4" width="16" height="11" fill="var(--paper)"/>
            <path d="M1 4l8 6 8-6" fill="none" stroke="var(--brand-green)" stroke-width="1.3"/>
          </svg>
        </li>
        <li class="contact-list__item">www.pivex.life
          <svg class="contact-list__icon" viewBox="0 0 18 18" aria-hidden="true">
            <circle cx="9" cy="9" r="7.5" fill="var(--paper)"/>
            <ellipse cx="9" cy="9" rx="3" ry="7.5" fill="none" stroke="var(--brand-green)" stroke-width="1.1"/>
            <path d="M1.5 9h15" stroke="var(--brand-green)" stroke-width="1.1"/>
          </svg>
        </li>
        <li class="contact-list__item">@pivex
          <svg class="contact-list__icon" viewBox="0 0 18 18" aria-hidden="true">
            <circle cx="9" cy="9" r="7" fill="var(--paper)"/>
          </svg>
        </li>
      </ul>
    </div>
  </section>

  <section class="card card--back" aria-label="Business card back">
    <div class="brand-lockup">
      <span class="brand-lockup__dot" aria-hidden="true"></span>
      <span class="wordmark">pivex</span>
    </div>
  </section>

</main>
</body>
</html>
```